Letterhead to Introduce a 'Sister' Company.

What I am needing is a design for a letter head to introduce our current customers base of (KT Alarm) customers to our new service, 'Kestrel Tide Solar Brokers'

```html
<!DOCTYPE html>
<html lang="en">
<head>
<meta charset="utf-8">
<title>Kestrel Tide Solar Brokers – Letterhead</title>
<link href="https://fonts.googleapis.com/css2?family=Montserrat:wght@400;600;700&family=Source+Sans+3:wght@900&display=swap" rel="stylesheet">
<style>
  :root {
    --navy: #004680;
    --orange: #fc9d06;
    --ink: #1a1a1a;
    --paper: #ffffff;
  }
  html, body {
    margin: 0;
    padding: 0;
    width: 1200px;
    height: 1200px;
    overflow: hidden;
    background: var(--paper);
  }
  .letterhead {
    position: relative;
    width: 1200px;
    height: 1200px;
    background: var(--paper);
    font-family: "Montserrat", Arial, sans-serif;
    color: var(--ink);
  }
  .side-bar {
    position: absolute;
    top: 0;
    width: 35px;
    height: 1200px;
    background: var(--navy);
  }
  .side-bar--left { left: 131px; }
  .side-bar--right { left: 1035px; }
  .top-band {
    position: absolute;
    left: 166px;
    top: 0;
    width: 869px;
    height: 33px;
    background: var(--orange);
  }
  .footer-band {
    position: absolute;
    left: 166px;
    top: 1149px;
    width: 869px;
    height: 51px;
    background: var(--orange);
    display: flex;
    align-items: center;
    justify-content: center;
    font-size: 27px;
    color: var(--ink);
    white-space: nowrap;
  }
  .brand {
    position: absolute;
    left: 606px;
    top: 50px;
    width: 402px;
    color: var(--navy);
    font-weight: 700;
    line-height: 1;
    text-align: center;
  }
  .brand__mark {
    display: block;
    width: 110px;
    height: 110px;
    border-radius: 50%;
    background: var(--orange);
    margin: 0 auto 36px;
  }
  .brand__name { display: block; font-size: 50px; letter-spacing: 1px; }
  .brand__sub {
    display: flex;
    align-items: center;
    gap: 8px;
    margin-top: 12px;
    font-size: 24px;
    letter-spacing: 4px;
    color: var(--orange);
    font-weight: 600;
  }
  .brand__sub::before,
  .brand__sub::after {
    content: "";
    flex: 1;
    height: 3px;
    background: var(--orange);
  }
  .heading {
    position: absolute;
    left: 249px;
    margin: 0;
    font-family: "Source Sans 3", Arial, sans-serif;
    font-weight: 900;
    color: var(--navy);
    line-height: 1;
  }
  .greeting { top: 265px; font-size: 26px; }
  .closing { top: 1022px; font-size: 27px; }
  .signature { top: 1074px; font-size: 27px; line-height: 38px; }
  .body-copy {
    position: absolute;
    left: 249px;
    top: 340px;
    margin: 0;
    font-size: 16.6px;
    line-height: 26.45px;
    white-space: nowrap;
  }
</style>
</head>
<body>
<main class="letterhead">
  <div class="top-band"></div>
  <div class="side-bar side-bar--left"></div>
  <div class="side-bar side-bar--right"></div>

  <div class="brand">
    <span class="brand__mark"></span>
    <span class="brand__name">KESTREL TIDE</span>
    <span class="brand__sub">SOLAR BROKERS</span>
  </div>

  <h1 class="heading greeting">Dear Members,</h1>

  <p class="body-copy">
    A striking, professional letterhead is a necessary communication<br>
    tool for individuals, brands and companies. Letterheads are<br>
    commonly used for memos and contracts–but beyond the<br>
    critical information they deliver–they are an important aspect<br>
    of a brands’ personality.<br>
    -<br>
    By combining visual elements with exceptional content, it’s<br>
    easy to make a professional impression on your clients and<br>
    customers. You can easily add your brand colors, logos, and<br>
    icons according to your profession or the type of company<br>
    you work for.<br>
    -<br>
    Depending on what your niche is you can create a letterhead<br>
    to reflect your corporate or quirky manner! The most important<br>
    thing is you create a great letterhead once–and commit to<br>
    using it continuously, and consistently–to strengthen each<br>
    impression of your brand.<br>
    -<br>
    The main details you’ll want to include in your letterhead is:<br>
    company name, physical address, and contact information.<br>
    The contact info can include your phone number, mobile<br>
    number, fax, and email address. You can also added various<br>
    fonts, borders, icons that fit well with your brand’s identity.<br>
    Type your text right into the fields provided or paste it from<br>
    another document.
  </p>

  <p class="heading closing">Sincerely,</p>
  <p class="heading signature">Martin Hale<br>Head of Alder Chess Society</p>

  <footer class="footer-band">PHONE: (555) 014-7720 EMAIL: hello@kestreltide.com</footer>
</main>
</body>
</html>
```